Income Tax Business Cards - Updates

Need to update these business cards while keeping all the same wording but just update them and make them look nicer and more modern/ on brand with our brand.

Industry/Entity Type

finance

Contact Information for Business Card

we have multiple locations so will just need to easily be able to change the address and phone numbers

Colors

Designer to choose colors to be used in the design.

```html
<!DOCTYPE html>
<html lang="en">
<head>
<meta charset="utf-8">
<title>Keystone Tax Group – Business Cards</title>
<link href="https://fonts.googleapis.com/css2?family=Montserrat:wght@400;500;600;700;800&display=swap" rel="stylesheet">
<style>
  :root {
    --brand-green: #0e4d2f;
    --brand-red: #c41f2b;
    --paper: #ffffff;
    --ink: #1a1a1a;
    --ink-soft: #333333;
    --backdrop: #eef0ee;
  }
  * { margin: 0; padding: 0; box-sizing: border-box; }
  html, body {
    width: 1200px;
    height: 1200px;
    overflow: hidden;
    background: var(--backdrop);
    font-family: "Montserrat", sans-serif;
  }
  .sheet {
    position: relative;
    width: 1200px;
    height: 1200px;
  }
  .card {
    position: absolute;
    left: 164px;
    width: 871px;
    height: 513px;
    display: block;
  }
  .card--front { top: 75px; }
  .card--back { top: 618px; }
  .card text { font-family: "Montserrat", sans-serif; }
  .headline-outlined {
    font-weight: 800;
    fill: var(--paper);
    stroke: var(--brand-red);
    stroke-width: 12px;
    stroke-linejoin: round;
    paint-order: stroke fill;
  }
  .headline-plain { font-weight: 500; fill: var(--paper); }
  .tagline { font-weight: 600; fill: var(--paper); }
  .cta { font-weight: 600; fill: var(--paper); }
  .phone { font-weight: 700; fill: var(--ink); }
  .address { font-weight: 400; fill: var(--ink-soft); }
  .brand-name { font-weight: 700; fill: var(--brand-green); }
  .fill-green { fill: var(--brand-green); }
  .fill-red { fill: var(--brand-red); }
  .fill-paper { fill: var(--paper); }
</style>
</head>
<body>
<main class="sheet">

  <!-- Front of card -->
  <svg class="card card--front" viewBox="0 0 871 513" role="group" aria-label="Business card front">
    <rect class="fill-paper" x="0" y="0" width="871" height="513"/>
    <rect class="fill-green" x="0" y="0" width="871" height="279"/>

    <text class="headline-outlined" x="56" y="122" font-size="92" textLength="578" lengthAdjust="spacingAndGlyphs">UP TO $6000</text>
    <text class="headline-plain" x="56" y="181" font-size="50" textLength="566" lengthAdjust="spacingAndGlyphs">SAME DAY ADVANCE</text>

    <polygon class="fill-red" points="466,213 871,213 871,279 440,279"/>
    <text class="tagline" x="56" y="257" font-size="20" textLength="362" lengthAdjust="spacingAndGlyphs">ON APPROVED TAX RETURNS!</text>
    <text class="cta" x="490" y="263" font-size="36" textLength="319" lengthAdjust="spacingAndGlyphs">FREE ESTIMATE</text>

    <text class="phone" x="467" y="327" font-size="35" textLength="310" lengthAdjust="spacingAndGlyphs">(555) 555-5555</text>
    <g class="phone-icon" transform="translate(790,306) scale(0.95)">
      <path class="fill-green" style="fill:var(--ink)" d="M4 1.5 L8 1 L10 6 L7.5 8 C9 11 11 13 14 14.5 L16 12 L21 14 L20.5 18 C20 19.5 18.5 20.5 17 20 C9 18 3 12 1.5 5 C1.2 3.5 2.3 1.8 4 1.5 Z"/>
      <path d="M13 2 A8 8 0 0 1 20 9" fill="none" stroke="var(--ink)" stroke-width="2"/>
      <path d="M13 6 A4 4 0 0 1 16 9" fill="none" stroke="var(--ink)" stroke-width="2"/>
    </g>

    <g class="address-block">
      <text class="address" x="616" y="366" font-size="20">Address Line 1</text>
      <text class="address" x="616" y="399" font-size="20">Address Line 1</text>
      <text class="address" x="616" y="432" font-size="20">Address Line 1</text>
      <text class="address" x="616" y="465" font-size="20">Address Line 1</text>
    </g>

    <g class="brand">
      <circle class="fill-red" cx="72" cy="404" r="16"/>
      <text class="brand-name" x="100" y="394" font-size="30">Keystone</text>
      <text class="brand-name" x="100" y="430" font-size="30">Tax Group</text>
    </g>
  </svg>

  <!-- Back of card -->
  <svg class="card card--back" viewBox="0 0 871 513" role="group" aria-label="Business card back">
    <rect class="fill-green" x="0" y="0" width="871" height="513"/>

    <text class="headline-plain" x="435" y="129" font-size="76" text-anchor="middle" textLength="456" lengthAdjust="spacingAndGlyphs">FILE YOUR</text>
    <text class="headline-outlined" x="435" y="214" font-size="80" text-anchor="middle" textLength="548" lengthAdjust="spacingAndGlyphs">TAXES HERE</text>

    <path class="fill-paper" d="M78 306 C230 268 440 254 766 276 L768 281 C460 270 250 284 82 312 Z"/>

    <text class="headline-outlined" x="435" y="392" font-size="92" text-anchor="middle" textLength="578" lengthAdjust="spacingAndGlyphs">UP TO $6000</text>
    <text class="headline-plain" x="435" y="457" font-size="50" text-anchor="middle" textLength="566" lengthAdjust="spacingAndGlyphs">SAME DAY ADVANCE</text>
  </svg>

</main>
</body>
</html>
```